Brochure Design- Targeted at Property Developers

We are the largest Conveyancing (property law) firm in the state of Victoria, Australia.

We need a very sophisticated brochure to enable us to take the next step and compete with law firms for property developer clients.

Much about us can be found on our website (inlcuding logos, photos, etc) www.trellowby.com.au but our business name is Trellowby- Marsh Vale not just Trellowby. ALSO I HAVE ATTACHED MANY PHOTOS OF OUR STAFF AND SOME LOGOS TO HELP!!

Size: fold (A3 double sided so that there is 4 A4 pages)

Copy:

This can be played with by the designer to spread across the 4 pages. Ideally the front page will be very minimalistic and not mention our brand (or at least the brand should not dominate):

Page 1: Do property developers have a genuine alternative to high legal fees?

Page 2 and 3:

- 100% of our developer clients recommend us
- We already look after the Conveyancing needs of more developers in Victoria than any other Conveyancing firm
- Industry benchmark off- the- plan contracts (tailored to the requirements of each development). Our special conditions (including variations, rebates and resale restrictions) are carefully chosen to protect the interests of our vendors while being commercially sensitive to ensure sales are not lost unnecessarily
- Expert in guiding developers from first time dual occupancies to seasoned developers of large scale land and highrise projects
- Our large team and highly refined systems ensure fastest possible settlement times after subdivision registration
- We are available to train your project marketers on completing and executing contracts so that sales are not delayed or lost
- Establishment of interest bearing trust accounts
- Before you buy a development site have us thoroughly investigate the contract and vendors statement. We can then conduct the purchase settlement on your behalf.
- We have the friendliest and most efficient staff. Every dealing you have with our dedicated Development Division will be prompt, professional and impressive. You will never need to follow us up!
- Highly experienced Conveyancers with the security of full Solicitor support

Please consider us next time you need Conveyancing.

Services options:
- Use us from contract preparation to settlement or;
- Have your Solicitor prepare the contract and use us as an alternative for the settlement stage only. Many Solicitors recommend us for this service already
- Fast subdivision lodgements (including obtaining mortgagee’s consent, Solicitor preparation of Land Titles Office application, owners corporation establishment)

Page 4: Just our contact details (see our website)

The design should make us look highly professional, conservative, yet cutting edge.

Target Market(s)

Property developers of small to medium sized land and unit developments

Industry/Entity Type

Security

Requirements
Must have
• - Our logo and contact details as well as the copy above.
Nice to have
• - Pictures of land sites, highrise buildings under construction
Should not have
• I really dislike overly corny photos where everyone is fake and smiling. Other photos would be great but not too cheesy.

```html
<!DOCTYPE html>
<html lang="en">
<head>
<meta charset="utf-8">
<title>Trellowby- Marsh Vale — Property Developer Brochure</title>
<link href="https://fonts.googleapis.com/css2?family=Russo+One&family=Arimo:wght@400;700&display=swap" rel="stylesheet">
<style>
  :root{
    --navy:#003a57;
    --orange:#c7662a;
    --white:#ffffff;
    --text-light:#e6eef3;
    --photo-light:#f2ede3;
    --photo-mid:#b6a68a;
    --photo-dark:#3a3327;
  }
  html,body{margin:0;padding:0;overflow:hidden;background:#fff;}
  .spread{position:relative;width:1200px;height:847px;overflow:hidden;font-family:"Arimo",Arial,sans-serif;}
  .back-cover{position:absolute;left:0;top:0;width:598px;height:847px;background:var(--navy);}
  .brand{position:absolute;left:58px;top:396px;display:flex;align-items:center;gap:7px;color:var(--white);}
  .brand-name{font-size:12px;line-height:13px;font-weight:400;}
  .brand-mark{width:11px;height:11px;background:var(--white);}
  .contact{position:absolute;left:56px;top:441px;color:var(--text-light);font-size:9.5px;line-height:11.6px;}
  .contact p{margin:0;}
  .contact dl{margin:0;display:grid;grid-template-columns:73px 14px auto;}
  .contact dt,.contact dd{margin:0;}
  .front-cover{position:absolute;left:598px;top:0;width:602px;height:847px;}
  .cover-photo{position:absolute;inset:0;
    background:linear-gradient(150deg,var(--photo-light) 0%,#e3d8c4 30%,var(--photo-mid) 55%,#7a6c56 78%,var(--photo-dark) 100%);}
  .headline-band{position:absolute;left:0;top:383px;width:602px;height:168px;background:var(--orange);opacity:.94;}
  .headline{position:absolute;left:42px;top:37px;margin:0;color:var(--white);
    font-family:"Russo One","Arial Black",sans-serif;font-weight:400;font-size:30px;line-height:40px;letter-spacing:.3px;}
</style>
</head>
<body>
<div class="spread">
  <section class="back-cover">
    <div class="brand">
      <span class="brand-name">Trellowby-<br>Marsh Vale</span>
      <span class="brand-mark"></span>
    </div>
    <div class="contact">
      <p>Level 4, 18 Calder Terrace</p>
      <p>Marsh Vale 3012 Victoria</p>
      <p>Australia</p>
      <p>(Off Wexley Road)</p>
      <dl>
        <dt>Postal</dt><dd>:</dd><dd>PO Box 4410 Wexley Road Central Marsh Vale 8016</dd>
        <dt>International</dt><dd>:</dd><dd>+61 3 9000 2417</dd>
        <dt>International Fax</dt><dd>:</dd><dd>+61 3 9000 2418</dd>
        <dt>Email</dt><dd>:</dd><dd>marshvale@trellowby.com.au</dd>
      </dl>
    </div>
  </section>
  <section class="front-cover">
    <div class="cover-photo" role="img" aria-label="Upward view of a glass high-rise facade with criss-crossing steel mullions in warm sepia tones"></div>
    <div class="headline-band">
      <h1 class="headline">DO PROPERTY DEVELOPERS<br>HAVE A GENUINE ALTERNATIVE<br>TO HIGH LEGAL FEES?</h1>
    </div>
  </section>
</div>
</body>
</html>
```